SALT PAN COMPUTERS AD DESIGN

This is to go into our local phone book as a full page (A4) advert.

NOTE THAT THE DEADLINE IS MIDNIGHT SUNDAY THE 29TH AUSSIE WA TIME NOT THE ADVERTISED DEADLINE AS FOR THE LIFE OF ME I CANT SEE WHERE TO CHANGE IT.

HAPPY TO PAY EXTRA FOR A "YES THATS IT" JOB.

Title - SALT PAN COMPUTERS

(THINGS TO HAVE)
24/7 FULL COMPUTER SERVICES
ALL COMPUTER PROBLEMS SOLVED
info@saltpancomputers.com.au
0400 13 8562
SALTPANCOMPUTERS.COM.AU
Virus's Removed
Data Recovery
Custom Computers and Programs built
Picked up & Dropped off
Private and Business Welcome

Maybe this photo - http://www.pixelvaultlib.com/stock-photo-22810457-attractive-receptionist.php?st=a3e91f2
with 24/7 service.

http://www.pixelvaultlib.com/stock-photo-22936104-hard-disk-drive-service.php?st=7d2f5e8 with Data Recovery

http://www.pixelvaultlib.com/stock-illustration-5318890-laptop.php?st=e14b7c9

I don't know but I have less than 40 hours to do this...

Been extented for another 50 hours cause they stuffed up also I have just opened a logo one as well.

Reason: As the publisher stuffed up with my account I now have an extra 50 hours !!

please note increased payment, this may increase again.

Reason: Not ment to finish for another 18 hours !!!!!!

Keep Going !!!!

only 5 hours left before it has to be at the printers !!!!

• only have 40 hours left from now. it must be in by 7am Monday 30th western aussie time. (not eastern aussie time)
• A 3D look
Colors like dark blue, bright yellow black and dark red.
modern look
modern font ie..HandelGothicBT etc

```html
<!DOCTYPE html>
<html lang="en">
<head>
<meta charset="utf-8">
<title>Salt Pan Computers – Full Page Advert</title>
<link href="https://fonts.googleapis.com/css2?family=Barlow:wght@400;500;700;800&family=PT+Sans:wght@700&display=swap" rel="stylesheet">
<style>
  :root {
    --ink: #000000;
    --burst: #b0122a;
    --burst-deep: #4a0610;
    --yellow: #fff200;
    --white: #ffffff;
    --navy: #1b2a8e;
    --red-text: #d4001a;
    --depth: #3a3a3a;
    --logo-text: #8c7f80;
    --photo-warm: #e9c9a4;
    --photo-steel: #b8bcc4;
    --photo-blue: #3d7fb8;
  }
  * { margin: 0; padding: 0; box-sizing: border-box; }
  html, body { width: 828px; height: 1200px; overflow: hidden; background: var(--ink); }
  .advert {
    position: relative;
    width: 828px; height: 1200px;
    overflow: hidden;
    font-family: "Barlow", "Helvetica Neue", Arial, sans-serif;
    background:
      radial-gradient(ellipse 420px 380px at 430px 560px, var(--burst) 0%, #7a0a1a 35%, var(--burst-deep) 65%, var(--ink) 100%);
  }
  .logo-area {
    position: absolute; left: 47px; top: 37px; width: 733px; height: 127px;
    background: var(--white);
    display: flex; align-items: center; justify-content: center;
  }
  .logo-name {
    font-family: "Barlow", Arial, sans-serif;
    font-weight: 500; font-size: 58px; letter-spacing: 2px;
    color: var(--logo-text);
  }
  .photo {
    position: absolute; border: 3px solid var(--white);
  }
  .photo--agent {
    left: 47px; top: 196px; width: 145px; height: 160px;
    background: linear-gradient(160deg, #f4f4f4 0%, var(--photo-warm) 55%, #2b2b2b 100%);
  }
  .photo--drive {
    left: 47px; top: 933px; width: 147px; height: 97px;
    background: linear-gradient(135deg, #f2f2f2 0%, var(--photo-steel) 60%, #5b5f66 100%);
  }
  .photo--keyboard {
    left: 47px; top: 1051px; width: 147px; height: 95px;
    background: linear-gradient(135deg, #dfe9f2 0%, var(--photo-blue) 70%, #173a5e 100%);
  }
  .headline {
    position: absolute; font-weight: 800; line-height: 1; white-space: nowrap;
  }
  .headline--hours {
    left: 208px; top: 168px; font-size: 228px; letter-spacing: 2px;
    color: var(--yellow);
    text-shadow: 3px 3px 0 #8a8200, 6px 6px 0 var(--depth);
  }
  .headline--services {
    left: 47px; top: 372px; font-size: 76px; font-weight: 500; letter-spacing: 3px;
    color: var(--white);
    text-shadow: 3px 3px 0 var(--depth);
  }
  .headline--all {
    left: 47px; top: 458px; font-size: 98px; font-weight: 800; letter-spacing: 2px;
    color: var(--yellow);
    text-shadow: 3px 3px 0 #8a8200, 5px 5px 0 var(--depth);
  }
  .headline--solved {
    left: 47px; top: 543px; font-size: 85px; font-weight: 400; letter-spacing: 2px;
    color: var(--white);
    text-shadow: 3px 3px 0 var(--depth);
  }
  .headline--solved strong { font-weight: 800; }
  .email-band {
    position: absolute; left: 42px; top: 648px; width: 741px; height: 52px;
    background: var(--navy);
    clip-path: polygon(0 0, 100% 0, 100% 100%, 26px 100%);
    display: flex; align-items: center; justify-content: flex-end; padding-right: 4px;
    font-size: 42px; font-weight: 500; letter-spacing: 1px; color: var(--yellow);
  }
  .phone {
    position: absolute; left: 47px; top: 718px; font-size: 124px; font-weight: 700;
    letter-spacing: 4px; line-height: 1; color: var(--white);
    text-shadow: 3px 3px 0 var(--depth), 5px 5px 0 #1a1a1a;
  }
  .web {
    position: absolute; left: 47px; top: 842px; font-size: 54px; font-weight: 800;
    letter-spacing: 2px; line-height: 1; color: var(--yellow);
    text-shadow: 2px 2px 0 var(--depth);
  }
  .service-list { list-style: none; }
  .service {
    position: absolute; left: 205px; width: 575px; height: 40px;
    clip-path: polygon(0 0, 100% 0, 100% 100%, 20px 100%);
    display: flex; align-items: center; padding-left: 28px;
    font-family: "PT Sans", Verdana, sans-serif; font-weight: 700; font-size: 27px;
  }
  .service--navy { background: var(--navy); color: var(--yellow); }
  .service--yellow { background: var(--yellow); color: var(--red-text); }
  .service:nth-child(1) { top: 933px; }
  .service:nth-child(2) { top: 990px; }
  .service:nth-child(3) { top: 1047px; }
  .service:nth-child(4) { top: 1104px; }
</style>
</head>
<body>
<main class="advert">
  <header class="logo-area">
    <span class="logo-name">SALT PAN COMPUTERS</span>
  </header>

  <div class="photo photo--agent" role="img" aria-label="Photo of a smiling support receptionist wearing a headset"></div>

  <h1 class="headline headline--hours">24/7</h1>
  <p class="headline headline--services">COMPUTER SERVICES</p>
  <p class="headline headline--all">ALL COMPUTER</p>
  <p class="headline headline--solved">PROBLEMS <strong>SOLVED</strong></p>

  <p class="email-band">info@saltpancomputers.com.au</p>
  <p class="phone">0400 13 8562</p>
  <p class="web">SALTPANCOMPUTERS.COM.AU</p>

  <div class="photo photo--drive" role="img" aria-label="Photo of gloved hands servicing an open hard disk drive"></div>
  <div class="photo photo--keyboard" role="img" aria-label="Close-up of a keyboard with a blue support key"></div>

  <ul class="service-list">
    <li class="service service--navy">Virus's Removed • Data Recovery</li>
    <li class="service service--yellow">Custom Computers &amp; Programs built</li>
    <li class="service service--navy">Picked up &amp; Dropped off</li>
    <li class="service service--yellow">Private and Business Welcome</li>
  </ul>
</main>
</body>
</html>
```